" A empresa é afiliada a Vantrel Investimentos e atua com produtos financeiros de investimentos: Fundos, Aplicaçoes de Renda Fixa, Açoes, Mercado Futuro e Derivativos. "

```html
<!DOCTYPE html>
<html lang="pt-BR">
<head>
<meta charset="UTF-8">
<title>Axial – Papel Timbrado</title>
<link href="https://fonts.googleapis.com/css2?family=Open+Sans:wght@300;400;600&display=swap" rel="stylesheet">
<style>
  :root {
    --backdrop: #e4e4e6;
    --paper: #ffffff;
    --paper-tint: #eef0f2;
    --ink-dark: #3a3d42;
    --ink-mid: #6b7079;
    --ink-light: #9aa0a8;
    --brand-blue: #3f6fa6;
    --mark-dark: #2b2d31;
    --rule: #d5d8dc;
  }
  * { margin: 0; padding: 0; box-sizing: border-box; }
  html, body {
    width: 1200px; height: 1200px; overflow: hidden;
    background: var(--backdrop);
    font-family: "Open Sans", Arial, sans-serif;
  }
  .letterhead {
    position: absolute;
    left: 211px; top: 50px;
    width: 778px; height: 1100px;
    background: linear-gradient(to bottom, var(--paper) 0%, var(--paper) 55%, var(--paper-tint) 100%);
    box-shadow: 0 4px 18px rgba(0,0,0,0.18);
  }
  .letterhead__top-rule {
    position: absolute; left: 0; right: 0; top: 152px;
    height: 1px; background: var(--rule);
  }
  .brand {
    position: absolute; left: 78px; top: 52px;
    display: flex; align-items: center; gap: 14px;
  }
  .brand__dot {
    width: 46px; height: 46px; border-radius: 50%;
    background: var(--brand-blue);
  }
  .brand__name {
    font-size: 38px; font-weight: 400; letter-spacing: 6px;
    color: var(--ink-dark); line-height: 1;
  }
  .brand__tagline {
    position: absolute; left: 140px; top: 104px;
    font-size: 9px; letter-spacing: 1.5px; text-transform: uppercase;
    color: var(--ink-mid);
  }
  .affiliate {
    position: absolute; left: 78px; top: 200px;
    display: flex; align-items: center; gap: 14px;
  }
  .affiliate__square {
    width: 80px; height: 80px; background: var(--mark-dark);
  }
  .affiliate__intro {
    font-size: 15px; font-weight: 300; color: var(--ink-mid);
  }
  .affiliate__name {
    font-size: 30px; font-weight: 300; color: var(--ink-mid);
    line-height: 1.1;
  }
  .affiliate__note {
    font-size: 8px; letter-spacing: 1px; text-transform: uppercase;
    color: var(--ink-light); margin-top: 4px;
  }
  .footer {
    position: absolute; left: 78px; right: 78px; top: 960px;
  }
  .footer__name {
    font-size: 22px; letter-spacing: 4px; color: var(--ink-dark);
  }
  .footer__tagline {
    font-size: 15px; color: var(--brand-blue); margin-top: 2px;
  }
  .footer__details {
    display: flex; margin-top: 28px; gap: 48px;
    font-size: 12px; line-height: 1.6;
  }
  .footer__address { color: var(--ink-mid); }
  .footer__contact { color: var(--brand-blue); }
</style>
</head>
<body>
  <main class="letterhead">
    <div class="brand">
      <span class="brand__dot"></span>
      <span class="brand__name">AXIAL</span>
    </div>
    <p class="brand__tagline">Agentes Autônomos de Investimentos</p>

    <div class="affiliate">
      <span class="affiliate__square"></span>
      <div>
        <p class="affiliate__intro">Um agente de investimento da</p>
        <p class="affiliate__name">Vantrel Investimentos</p>
        <p class="affiliate__note">Corretora de valores desde 2001</p>
      </div>
    </div>

    <footer class="footer">
      <p class="footer__name">AXIAL</p>
      <p class="footer__tagline">Agentes Autônomos De Investimentos</p>
      <div class="footer__details">
        <address class="footer__address" style="font-style:normal">
          R. das Acácias Altas, 415 Cj. 88<br>
          Vila Serena - São Paulo-SP - CEP: 04512-030
        </address>
        <div class="footer__contact">
          (11) 3870-5146<br>
          contato@axialinvest.com.br<br>
          www.axialinvestimentos.com.br
        </div>
      </div>
    </footer>
  </main>
</body>
</html>
```